B2B flyer solution for charging infrastructures (One-Pager Din A4, double-sided)

We need a professional design for our flyer in format Din A4/both sides.
Attached you will find the content for the flyer, but we are looking for a modern, professional design.

Some background/context information:
- the product is about a solution for charging and billing of charging infrastructures (for electric cars) in companies
- target group: companies, esp. facility managers, fleet managers, controlling, CTO, CEO
- should be printed and available online
- our website (and most of our current design work): https://wendo-kraft.de

In the files you will find:
- photos of reference implementations of our solution (should be included in the flyer)
- stock photos (we are using the one you will find in the current flyer on our presentations, maybe you can use it too to keep some corporate identity.
- our logo
- the current flyer as PDF and as PowerPoint
- a sample presentation we also need for customer communication

It would be nice if the design will align with the existing design work, but bring fresh aspects and will be up-to-date and professional.

Target Market(s)

B2B, companies, fleet managers, facility managers, CTO, CIO

Industry/Entity Type

Enterprises, Charging Solutions for Electric Vehicles

Requirements
Nice to have
• Bright, light design, clean, readable

```html
<!DOCTYPE html>
<html lang="de">
<head>
<meta charset="utf-8">
<title>Wendo-Kraft Professional – Flyer Vorder- und Rückseite</title>
<link rel="stylesheet" href="https://fonts.googleapis.com/css2?family=Poppins:wght@300;400;500;700;800&family=Arimo:wght@400;700&display=swap">
<style>
:root{
  --navy:#1b1d2e;
  --navy-soft:#25283b;
  --purple:#6a4fd0;
  --magenta:#d21fbf;
  --band:#efeff2;
  --ink:#1e1f26;
  --rule:#b9bac2;
  --backdrop:#ffffff;
}
*{margin:0;padding:0;box-sizing:border-box}
html,body{width:747px;height:1200px;overflow:hidden;background:var(--backdrop)}
.sheet{position:absolute;top:380px;width:647px;height:837px;background:#fff;transform-origin:0 0;transform:scale(.525);
  box-shadow:0 6px 24px rgba(0,0,0,.18);font-family:"Arimo",Arial,sans-serif;color:var(--ink);overflow:hidden}
.sheet-front{left:22px}
.sheet-back{left:385px}
.abs{position:absolute}
.poppins{font-family:"Poppins",sans-serif}
.purple{color:var(--purple)}
.magenta{color:var(--magenta)}

/* front */
.hero{left:0;top:0;width:647px;height:287px;background:linear-gradient(160deg,var(--navy-soft),var(--navy));color:#fff;text-align:center}
.brand{left:0;right:0;top:92px;display:flex;justify-content:center;align-items:center;gap:10px;font-family:"Poppins",sans-serif;font-size:29px;font-weight:400}
.brand-dot{width:13px;height:13px;border-radius:50%;background:var(--magenta)}
.hero-title{left:0;right:0;top:158px;font-family:"Poppins",sans-serif;font-weight:800;font-size:35px;letter-spacing:.5px}
.hero-sub{left:80px;right:80px;top:217px;font-family:"Poppins",sans-serif;font-weight:300;font-size:16px;line-height:19px}
.intro{left:0;top:287px;width:647px;height:101px;background:var(--band)}
.intro-art{left:22px;top:33px;width:133px;height:42px;border-radius:8px;background:linear-gradient(90deg,#3b3d47,#6a6c76)}
.intro-text{left:175px;top:30px;width:440px;font-size:11px;line-height:17px}
.heading{font-family:"Poppins",sans-serif;font-weight:400;font-size:19px;line-height:25px}
.heading span{display:block}
.ticks{list-style:none}
.ticks li{position:relative;padding-left:26px;font-size:8.5px;line-height:11px}
.ticks svg{position:absolute;left:0;top:1px;width:10px;height:10px}
.benefits-head{left:30px;top:410px}
.benefits{left:27px;top:490px;width:300px}
.benefits li{margin-bottom:13px}
.services-head{left:340px;top:410px}
.services{left:341px;top:452px;width:260px}
.services li{margin-bottom:11px;font-size:7.5px;line-height:10px}
.contact{left:0;top:602px;width:343px;height:166px;background:var(--band)}
.contact-rule{left:27px;top:38px;width:1px;height:88px;background:var(--ink)}
.contact-head{left:47px;top:34px;font-family:"Poppins",sans-serif}
.contact-head .a{display:block;font-size:15px;line-height:17px;color:var(--purple)}
.contact-head .b{display:block;font-size:22px;line-height:22px;color:var(--magenta)}
.contact-text{left:47px;top:92px;width:250px;font-size:7.8px;line-height:10px}
.photo-car{left:343px;top:586px;width:246px;height:182px;background:linear-gradient(135deg,#9a9ca3 0%,#4c4e57 45%,#2a2b31 100%)}

/* footer shared */
.footer{left:0;bottom:0;width:647px;height:66px;background:var(--navy);color:#fff;display:flex;align-items:center}
.f-item{display:flex;align-items:center;gap:10px;font-size:10px}
.f-phone{padding-left:28px;width:268px}
.f-phone span{color:var(--magenta);font-weight:700;font-size:17px}
.f-web{width:160px;height:40px;border-left:1px solid #3c3f55;justify-content:center}
.f-mail{flex:1;height:40px;border-left:1px solid #3c3f55;justify-content:center}

/* back */
.back-title{left:30px;top:30px;font-family:"Poppins",sans-serif;font-weight:800;font-size:35px;letter-spacing:.5px;line-height:42px}
.back-sub{left:28px;top:76px;font-family:"Poppins",sans-serif;font-size:26px;line-height:32px}
.back-rule{left:30px;top:128px;width:558px;height:1px;background:var(--rule)}
.sub-rule{left:346px;top:368px;width:262px;height:1px;background:var(--rule)}
.h2{font-family:"Poppins",sans-serif;font-size:13.5px;line-height:17px}
.h2 span{display:block}
.para{font-size:8px;line-height:10.5px}
.usage-head{left:24px;top:148px}
.usage{left:24px;top:198px;width:300px;height:110px}
.usage-item{position:absolute;display:flex;align-items:center;gap:14px;font-size:8px;line-height:10px}
.service-head{left:24px;top:332px}
.service-text{left:24px;top:378px;width:260px}
.service-list{left:24px;top:432px}
.service-list li{margin-bottom:4px;font-size:8px;line-height:10.5px;padding-left:22px}
.photo-posts{left:24px;top:533px;width:251px;height:147px;background:linear-gradient(135deg,#c89a52 0%,#6d7a55 45%,#2f3130 100%)}
.caption{left:28px;top:713px;padding-left:12px;border-left:2px solid var(--magenta);font-weight:700;font-size:11px;line-height:15px}
.integ-head{left:346px;top:155px}
.integ-text{left:346px;top:203px;width:260px}
.integ-list{left:346px;top:240px;width:275px}
.integ-list li{margin-bottom:9px;font-size:7.5px;line-height:10px;padding-left:20px}
.owner-head{left:346px;top:390px}
.owner-text{left:346px;top:430px;width:270px}
.owner-list{left:346px;top:482px;width:250px}
.owner-list li{margin-bottom:12px;font-size:7.5px;line-height:10px;padding-left:20px}
.photo-garage{left:348px;top:598px;width:250px;height:148px;background:linear-gradient(90deg,#6e7064 0%,#3a3c38 60%,#9aa0a2 100%)}
</style>
</head>
<body>
<svg width="0" height="0" style="position:absolute">
  <symbol id="tick" viewBox="0 0 12 12"><circle cx="6" cy="6" r="6" fill="#1e1f26"/><path d="M3.3 6.2l1.8 1.8 3.6-3.8" stroke="#fff" stroke-width="1.5" fill="none"/></symbol>
  <symbol id="phone" viewBox="0 0 24 24"><path d="M6.6 10.8a15.2 15.2 0 006.6 6.6l2.2-2.2c.3-.3.7-.4 1-.2 1.1.4 2.3.6 3.6.6.6 0 1 .4 1 1V20c0 .6-.4 1-1 1A17 17 0 013 4c0-.6.4-1 1-1h3.5c.6 0 1 .4 1 1 0 1.3.2 2.5.6 3.6.1.3 0 .7-.2 1z" fill="#fff"/></symbol>
  <symbol id="globe" viewBox="0 0 24 24"><g fill="none" stroke="#fff" stroke-width="2"><circle cx="12" cy="12" r="10"/><path d="M2 12h20M12 2c3 3 3 17 0 20M12 2c-3 3-3 17 0 20"/></g></symbol>
  <symbol id="mail" viewBox="0 0 24 18"><g fill="none" stroke="#fff" stroke-width="2"><rect x="1" y="1" width="22" height="16"/><path d="M1 1l11 9 11-9"/></g></symbol>
</svg>

<!-- front side -->
<main class="sheet sheet-front">
  <header class="abs hero">
    <div class="abs brand"><span class="brand-dot"></span>wendo-kraft.de</div>
    <h1 class="abs hero-title">WENDO-KRAFT PROFESSIONAL</h1>
    <p class="abs hero-sub">die maßgeschneiderte B2B-Abrechnungslösung für Elektro-mobilität</p>
  </header>

  <section class="abs intro">
    <div class="abs intro-art" role="img" aria-label="Illustration: Reihe von Firmenfahrzeugen"></div>
    <p class="abs intro-text">Lade-Infrastruktur-Abrechnungslösungen für Unternehmen, damit Lade-Infrastruktur Erträge statt Kosten produziert. So wird Lade-Infrastruktur von einer Kostenstelle zu einem Profitcenter.</p>
  </section>

  <h2 class="abs heading benefits-head"><span class="purple">Mit wendo-kraft</span><span class="magenta">Professional profitieren:</span></h2>
  <ul class="abs ticks benefits">
    <li><svg><use href="#tick"/></svg>Effizienter Verwaltung von Lade-Infrastruktur</li>
    <li><svg><use href="#tick"/></svg>Umfassende Full-Service-Betreuung</li>
    <li><svg><use href="#tick"/></svg>Nahtloser Integration in Ihre kaufmännischen Prozesse</li>
    <li><svg><use href="#tick"/></svg>Vielseitigen Abrechnungsmöglichkeiten</li>
  </ul>

  <h2 class="abs heading services-head"><span class="magenta">Leistungen:</span></h2>
  <ul class="abs ticks services">
    <li><svg><use href="#tick"/></svg>Vielseitige Abrechnungsmöglichkeiten für Fuhrpark, Mitarbeiter, Partnerunternehmen, Mieter, Kunden und andere.</li>
    <li><svg><use href="#tick"/></svg>Full-Service-Betreuung (Monitoring, Abrechnung, Benutzerbetreuung)</li>
    <li><svg><use href="#tick"/></svg>Integration in Ihre Unternehmensabläufe</li>
    <li><svg><use href="#tick"/></svg>Berücksichtigung von Eigentümer/Mieter-Konstellatione</li>
  </ul>

  <section class="abs contact">
    <div class="abs contact-rule"></div>
    <h2 class="abs contact-head"><span class="a">Kontaktieren</span><span class="b">Sie uns</span></h2>
    <p class="abs contact-text">Erfahren Sie mehr über wendo-kraft und wie wir Ihre Abrechnungsanforderungen erfüllen können. Kontaktieren Sie uns für eine kostenlose Beratung</p>
  </section>
  <div class="abs photo-car" role="img" aria-label="Foto: dunkles Elektroauto an einer Wandladestation in einer Tiefgarage"></div>

  <footer class="abs footer">
    <div class="f-item f-phone"><svg width="20" height="20"><use href="#phone"/></svg><span>+49 (0) 3210 987 654</span></div>
    <div class="f-item f-web"><svg width="11" height="11"><use href="#globe"/></svg>www.wendo-kraft.de</div>
    <div class="f-item f-mail"><svg width="13" height="10"><use href="#mail"/></svg>info@wendo-kraft.de</div>
  </footer>
</main>

<!-- back side -->
<main class="sheet sheet-back">
  <h1 class="abs back-title"><span class="purple">WENDO-KRAFT</span> <span class="magenta">PROFESSIONAL</span></h1>
  <p class="abs back-sub">die Funktionen im Überblick</p>
  <div class="abs back-rule"></div>

  <h2 class="abs h2 usage-head"><span>Verrechnung von</span><span class="magenta">Ladevorgängen für:</span></h2>
  <div class="abs usage">
    <div class="usage-item" style="left:0;top:10px">
      <svg width="38" height="26" viewBox="0 0 38 26"><path d="M6 12l4-9h18l4 9h3v9h-4v4h-5v-4H13v4H8v-4H3v-9z" fill="#8a4fd8"/><rect x="11" y="5" width="16" height="6" fill="#fff"/><circle cx="9" cy="16" r="2" fill="#fff"/><circle cx="29" cy="16" r="2" fill="#fff"/></svg>
      <span>Fuhrpark,<br>Dienstwagen</span></div>
    <div class="usage-item" style="left:140px;top:8px">
      <svg width="36" height="30" viewBox="0 0 36 30"><circle cx="18" cy="7" r="6" fill="#a345d4"/><circle cx="7" cy="11" r="4" fill="#a345d4"/><circle cx="29" cy="11" r="4" fill="#a345d4"/><path d="M8 30V21a10 10 0 0120 0v9zM0 30v-8a7 7 0 0110-4v12zM36 30v-8a7 7 0 00-10-4v12z" fill="#a345d4"/></svg>
      <span>Mitarbeiter<br>Privatfahrzeuge</span></div>
    <div class="usage-item" style="left:3px;top:62px">
      <svg width="34" height="40" viewBox="0 0 34 40"><rect x="2" y="8" width="14" height="32" fill="#9a45d6"/><rect x="16" y="16" width="16" height="24" fill="#9a45d6"/><rect x="5" y="2" width="6" height="6" fill="#9a45d6"/><g fill="#fff"><rect x="5" y="12" width="3" height="3"/><rect x="10" y="12" width="3" height="3"/><rect x="5" y="19" width="3" height="3"/><rect x="10" y="19" width="3" height="3"/><rect x="20" y="20" width="3" height="3"/><rect x="26" y="20" width="3" height="3"/><rect x="20" y="27" width="3" height="3"/><rect x="26" y="27" width="3" height="3"/></g></svg>
      <span>Vermieter,<br>Eigentümer</span></div>
    <div class="usage-item" style="left:140px;top:62px">
      <svg width="38" height="34" viewBox="0 0 38 34"><circle cx="19" cy="6" r="5" fill="#a345d4"/><circle cx="9" cy="12" r="5" fill="#a345d4"/><circle cx="29" cy="12" r="5" fill="#a345d4"/><circle cx="19" cy="18" r="5" fill="#a345d4"/><path d="M9 34a10 10 0 0120 0zM0 28a9 9 0 0114-6v6zM38 28a9 9 0 00-14-6v6z" fill="#a345d4"/></svg>
      <span>Kunden und<br>Gäste</span></div>
  </div>

  <h2 class="abs h2 service-head"><span>Full-Service-Betreuung</span><span class="magenta">für sorgenfreies Management</span></h2>
  <p class="abs para service-text">wendo-kraft übernimmt auf Wunsch alle organisatorischen Belange bei der Verwaltung Ihrer Lade-Infrastruktur, einschließlich:</p>
  <ul class="abs ticks service-list">
    <li><svg><use href="#tick"/></svg>Monitoring</li>
    <li><svg><use href="#tick"/></svg>Support</li>
    <li><svg><use href="#tick"/></svg>User-Onboarding und -Support</li>
    <li><svg><use href="#tick"/></svg>Handling von Zugangskarten</li>
    <li><svg><use href="#tick"/></svg>Integration von firmeninternen Zugangstoken</li>
  </ul>
  <div class="abs photo-posts" role="img" aria-label="Foto: Reihe von Ladesäulen auf einem Parkplatz im Abendlicht"></div>
  <p class="abs caption">wendo-kraft - Die Abrechnungslösung für<br>Lade-Infrastruktur in Unternehmen</p>

  <h2 class="abs h2 integ-head"><span>Perfekte Integration in</span><span class="magenta">kaufmännische Prozesse</span></h2>
  <p class="abs para integ-text">wendo-kraft fügt sich nahtlos in die kaufmännischen Strukturen moderner Unternehmen ein und bietet:</p>
  <ul class="abs ticks integ-list">
    <li><svg><use href="#tick"/></svg>Erweitertes Reporting</li>
    <li><svg><use href="#tick"/></svg>Aufschlüsselung und Tarifierung nach Nutzergruppe</li>
    <li><svg><use href="#tick"/></svg>Unterstützung unternehmensinterner Abrechnung und Verrechnung und/oder Zahlungseinzug durch wendo-kraft</li>
    <li><svg><use href="#tick"/></svg>Schnittstellen zu Buchhaltung und Lohnbuchhaltung</li>
    <li><svg><use href="#tick"/></svg>Bedarfsgerechte Anpassbarkeit</li>
  </ul>
  <div class="abs sub-rule"></div>

  <h2 class="abs h2 owner-head"><span>Besonderer Aspekt: Eigentümer-</span><span class="magenta">Mieter-Konstellationen</span></h2>
  <p class="abs para owner-text">Häufige Situation: Der Mieter eines Objektes benötigt Lade-Infrastruktur, der Eigentümer/Verwalter möchte nicht zusätzlich belastet werden.</p>
  <ul class="abs ticks owner-list">
    <li><svg><use href="#tick"/></svg>Unterschiedliche Betreibermodelle für verschiedene Situationen (Langzeit-Mieter vs. Kurzzeit-Mieter)</li>
    <li><svg><use href="#tick"/></svg>Kauf-, Miet- und Leasing-Optionen</li>
    <li><svg><use href="#tick"/></svg>Kostenneutral für Eigentümer/Verwalter durch geeignete Abrechnungsmodelle</li>
  </ul>
  <div class="abs photo-garage" role="img" aria-label="Foto: Wandladestation mit eingestecktem Ladekabel in einem Parkhaus"></div>

  <footer class="abs footer">
    <div class="f-item f-phone"><svg width="20" height="20"><use href="#phone"/></svg><span>+49 (0) 3210 987 654</span></div>
    <div class="f-item f-web"><svg width="11" height="11"><use href="#globe"/></svg>www.wendo-kraft.de</div>
    <div class="f-item f-mail"><svg width="13" height="10"><use href="#mail"/></svg>info@wendo-kraft.de</div>
  </footer>
</main>
</body>
</html>
```